Cannabis Company needs a packaging design for a 4x6 pouch

We need a design for a new cannabis company. Included is the logo in red. The logo color can change. Whatever color looks best with the design is what we'll use. The design can't include any cartoon characters or anything that may appeal to children. We have multiple products that are similar that will be using the same design. The pouch will contain 10 pyramid shaped gummies. The look we're going for is modern, simple, but eye catching. I included a handful of photos of packaging we like if that helps.

```html
<!DOCTYPE html>
<html lang="en">
<head>
<meta charset="utf-8">
<title>Halvard – Blueberry Cannabis-Infused Gummy Pouch</title>
<link rel="stylesheet" href="https://fonts.googleapis.com/css2?family=Staatliches&family=Roboto+Condensed:wght@400;700&family=Roboto+Mono:wght@500;700&display=swap">
<style>
  :root {
    --navy-deep: #0d1238;
    --navy: #1b2a78;
    --berry: #3f5fc8;
    --berry-light: #7d9be6;
    --teal: #4fae9e;
    --teal-dark: #2c6f6a;
    --ink: #1f1a8c;
    --panel: #ffffff;
    --brand-red: #d0242a;
  }
  * { margin: 0; padding: 0; box-sizing: border-box; }
  html, body { width: 702px; height: 1200px; overflow: hidden; background: var(--navy-deep); }
  .pouch {
    position: relative;
    width: 702px;
    height: 1200px;
    overflow: hidden;
  }
  .artwork {
    position: absolute;
    inset: 0;
    background:
      radial-gradient(circle at 20% 8%, var(--berry) 0 14%, transparent 15%),
      radial-gradient(circle at 92% 22%, var(--berry) 0 16%, transparent 17%),
      radial-gradient(circle at 10% 90%, var(--berry) 0 20%, transparent 21%),
      radial-gradient(circle at 84% 70%, var(--berry) 0 22%, transparent 23%),
      linear-gradient(155deg, var(--teal-dark) 0%, var(--navy) 35%, var(--teal) 55%, var(--navy-deep) 80%);
  }
  .label-panel {
    position: absolute;
    left: 98px;
    top: 414px;
    width: 529px;
    height: 288px;
    background: var(--panel);
    text-align: center;
  }
  .brand-badge {
    position: absolute;
    left: 257px;
    top: 318px;
    width: 188px;
    height: 131px;
    background: var(--panel);
    border: 3px solid var(--brand-red);
    display: flex;
    align-items: center;
    justify-content: center;
    z-index: 2;
  }
  .brand-name {
    font-family: "Roboto Condensed", sans-serif;
    font-weight: 700;
    font-size: 40px;
    color: var(--brand-red);
    letter-spacing: 1px;
  }
  .product-flavor {
    position: absolute;
    top: 38px;
    left: 0;
    right: 0;
    font-family: "Staatliches", sans-serif;
    font-size: 92px;
    line-height: 1;
    letter-spacing: 6px;
    color: var(--ink);
  }
  .product-type {
    position: absolute;
    left: 31px;
    right: 42px;
    top: 113px;
    height: 46px;
    background: var(--ink);
    color: #fff;
    font-family: "Roboto Mono", monospace;
    font-weight: 700;
    font-size: 26px;
    line-height: 46px;
  }
  .product-facts {
    position: absolute;
    left: 31px;
    right: 42px;
    top: 190px;
    display: flex;
    align-items: center;
    justify-content: space-between;
    font-family: "Roboto Mono", monospace;
    font-weight: 700;
    color: var(--ink);
  }
  .fact { display: flex; align-items: baseline; gap: 5px; font-size: 30px; }
  .fact small { font-size: 17px; font-weight: 500; }
  .divider { width: 2px; height: 48px; background: var(--ink); }
  .warning {
    font-family: "Roboto Condensed", sans-serif;
    font-weight: 400;
    font-size: 16px;
    line-height: 1.15;
    text-align: left;
  }
</style>
</head>
<body>
  <main class="pouch">
    <div class="artwork" role="img" aria-label="Illustrated background of large stylised blueberries among flowing teal and navy swirls"></div>

    <div class="brand-badge">
      <span class="brand-name">halvard</span>
    </div>

    <section class="label-panel">
      <h1 class="product-flavor">Blueberry</h1>
      <p class="product-type">Cannabis – infused gummy</p>
      <div class="product-facts">
        <span class="fact">10 <small>count</small></span>
        <span class="divider"></span>
        <span class="fact">50 <small>MG</small></span>
        <span class="divider"></span>
        <span class="fact">THC</span>
        <span class="divider"></span>
        <span class="warning">21+ Not safe<br>for children</span>
      </div>
    </section>
  </main>
</body>
</html>
```